・大阪らしい闊達で明るいイメージ
・2025年開催予定のひかり環境博覧祭に向けて変わっていく新しい大阪のイメージ
・一目で南学競のパンフレットとわかるようなデザイン
・コロナ禍からの復活の象徴となる、ハンパなく熱い大会を彷彿とさせるデザイン
にしたいと思ってます。オリジナル・未発表の作品でお願い致します。

また、記載項目といたしまして
・表紙には以下の4項目を必ず記載してください。
1. 燃えまくり!!南学競
※阪には「はん」と上にふりがなをつけてください
※ぇは小さい「え」です
2. 開催日程:2023年7月31日(月)~8月25日(金)
3. 第75回南部医療学徒連合競技祭
4. 代表主管校:緑丘学院大学
・裏表紙には以下の2項目を必ず記載してください。
1. 〒999-0412 大阪府吹田市桜野台9丁目4 緑丘学院大学第75回南学競運営室
2. 第75回南部医療学徒連合競技祭運営委員会
B5
4ページ
• イラストレーター形式 (.ai)
・ページ数は4ページとしておりますが、デザインがそろっていれば何ページでも構いません。
・イラストはイラストレーター形式にて縦長仕様でお願いします。
・そのまま印刷会社に入稿するので、カラーモードはCMYKにて、塗り足し・アウトライン化もお願いします。
・ご提案を選択後、当選者様に修正を依頼する可能性がございますのでご了承ください。
・選択させていただいたデザインの著作権(財産権)等の扱いはDraftora利用規約に従い、弊運営委員会への譲渡をお願いします。
・以下に過去大会の総合パンフレットデザインを添付いたします。
・その他、何かご不明な点などございましたら、お気軽にご相談ください。
第72回、70回南学競のパンフレットデザインを添付いたします。

・「燃えまくり!!南学競」のスローガンに合う明るく勢いのあるデザイン
・一目で体育大会のポスターだとわかるデザイン
・星影の柱は緑丘学院大学(吹田キャンパス)の近くにあり、主管校の地域を反映したデザインになっている
・ポスター、パンフレットの表紙にふさわしい、シンプルながらも目をひくデザイン
・修正の依頼にもご丁寧に対応していただき、よりよいデザインに仕上げてくださった

以上の点からぴの様のデザインを選ばせていただきました。

たくさんのご応募をいただき、心より感謝申し上げます。
当選作品を選ぶのが非常に困難でしたが、どれも素晴らしいデザインでした。
来年も南学競のポスター・パンフレットデザインを募集することがあるかもしれません。
その際は、ぜひまたみなさまのご応募をお待ちしております。

今回のご参加、そして素晴らしい作品をご提案していただき、誠にありがとうございました。

```html
<!DOCTYPE html>
<html lang="ja">
<head>
<meta charset="utf-8">
<title>燃えまくり!!南学競 第75回南部医療学徒連合競技祭</title>
<link rel="stylesheet" href="https://fonts.googleapis.com/css2?family=Yuji+Boku&family=Noto+Sans+JP:wght@500;700;900&display=swap">
<style>
  :root {
    --night: #0b0806;
    --ember: #f08a24;
    --flame: #ffb347;
    --deep-fire: #b8360c;
    --white: #ffffff;
    --accent-red: #e23a1e;
    --ink: #111111;
  }
  * { margin: 0; padding: 0; box-sizing: border-box; }
  html, body { width: 851px; height: 1200px; overflow: hidden; background: var(--night); }
  .poster {
    position: relative;
    width: 851px;
    height: 1200px;
    overflow: hidden;
    background: var(--night);
    font-family: "Noto Sans JP", sans-serif;
    color: var(--white);
  }
  .track-backdrop {
    position: absolute;
    inset: 0;
    background:
      radial-gradient(ellipse 520px 160px at 330px 560px, rgba(184,54,12,0.55), transparent 75%),
      radial-gradient(ellipse 300px 220px at 230px 760px, rgba(240,138,36,0.35), transparent 70%),
      linear-gradient(180deg, #1d140d 0%, #0e0a07 40%, #140c07 70%, #0b0806 100%);
  }
  .runner-upper {
    position: absolute;
    left: 0;
    top: 0;
    width: 851px;
    height: 560px;
    background:
      radial-gradient(ellipse 230px 140px at 430px 330px, rgba(255,200,110,0.75), transparent 70%),
      radial-gradient(ellipse 300px 200px at 300px 420px, rgba(240,138,36,0.8), transparent 72%),
      radial-gradient(ellipse 180px 260px at 160px 160px, rgba(240,138,36,0.55), transparent 72%),
      radial-gradient(ellipse 200px 260px at 720px 180px, rgba(184,54,12,0.45), transparent 72%),
      linear-gradient(160deg, rgba(60,40,28,0.6) 0%, rgba(40,26,18,0.3) 50%, transparent 100%);
  }
  .runner-lower {
    position: absolute;
    left: 180px;
    top: 620px;
    width: 671px;
    height: 580px;
    background:
      radial-gradient(ellipse 180px 220px at 290px 330px, rgba(255,210,130,0.8), transparent 70%),
      radial-gradient(ellipse 300px 260px at 330px 360px, rgba(240,138,36,0.85), transparent 72%),
      linear-gradient(155deg, transparent 25%, rgba(230,200,170,0.35) 40%, rgba(240,138,36,0.55) 55%, transparent 75%),
      radial-gradient(ellipse 280px 200px at 560px 120px, rgba(184,54,12,0.55), transparent 72%);
  }
  .slogan {
    position: absolute;
    left: 82px;
    top: 405px;
    font-family: "Yuji Boku", serif;
    font-size: 118px;
    line-height: 1;
    letter-spacing: -4px;
    color: var(--white);
    text-shadow: 0 0 22px rgba(240,138,36,0.95), 0 0 6px rgba(255,179,71,0.9);
    white-space: nowrap;
  }
  .slogan ruby rt {
    font-family: "Noto Sans JP", sans-serif;
    font-size: 22px;
    font-weight: 700;
    color: var(--accent-red);
    text-shadow: none;
    letter-spacing: 0;
  }
  .event-nickname {
    position: absolute;
    right: 100px;
    top: 560px;
    font-family: "Yuji Boku", serif;
    font-size: 72px;
    line-height: 1;
    text-shadow: 0 0 16px rgba(240,138,36,0.9);
  }
  .event-name {
    position: absolute;
    left: 128px;
    top: 660px;
    font-weight: 900;
    font-size: 29px;
    white-space: nowrap;
    text-shadow: 0 0 8px rgba(0,0,0,0.8);
  }
  .event-name .edition { margin-right: 12px; font-size: 30px; }
  .event-name .edition b { color: var(--flame); font-size: 44px; }
  .schedule {
    position: absolute;
    left: 112px;
    top: 905px;
    font-weight: 900;
    line-height: 1.08;
    text-shadow: 0 0 8px rgba(0,0,0,0.8);
  }
  .schedule .year { font-size: 42px; }
  .schedule .date { font-size: 64px; letter-spacing: -1px; }
  .schedule .date .dow { font-size: 40px; }
  .host {
    display: flex;
    align-items: center;
    gap: 10px;
    margin-top: 8px;
    font-size: 24px;
    font-weight: 700;
  }
  .host .host-label {
    background: var(--white);
    color: var(--ink);
    font-size: 13px;
    font-weight: 700;
    padding: 2px 6px;
  }
</style>
</head>
<body>
<main class="poster">
  <div class="track-backdrop" role="img" aria-label="火の粉が舞う暗い陸上トラック"></div>
  <div class="runner-upper" role="img" aria-label="炎に包まれて走る選手の脚とランニングシューズ"></div>
  <div class="runner-lower" role="img" aria-label="炎をまとって踏み出す選手の脚とスパイク"></div>

  <h1 class="slogan"><ruby>燃<rt>も</rt></ruby>えまくり!!</h1>
  <p class="event-nickname">南学競</p>
  <p class="event-name"><span class="edition">第<b>75</b>回</span>南部医療学徒連合競技祭</p>

  <section class="schedule">
    <p class="year">2023年</p>
    <p class="date">7月31日<span class="dow">(月)</span>～</p>
    <p class="date">8月25日<span class="dow">(金)</span></p>
    <p class="host"><span class="host-label">代表主管校</span>緑丘学院大学</p>
  </section>
</main>
</body>
</html>
```